Letterhead design for business

Looking for an attractive and professional letterhead that uses the logo that is attached below.

Target Market(s)

Potential bankruptcy clients.

Industry/Entity Type

Legal

Colors

Designer to choose colors to be used in the design.

Requirements
Must have
• Address for locations, phone number, and website address.
• Addresses are on website ferncoveadvice.example. Use following phone number (for tracking purposes): 555-013-8274

```html
<!DOCTYPE html>
<html lang="en">
<head>
<meta charset="utf-8">
<title>Fern Cove Law Group – Letterhead</title>
<link href="https://fonts.googleapis.com/css2?family=Lato:wght@400;700&display=swap" rel="stylesheet">
<style>
  :root {
    --backdrop: #dccdb4;
    --paper: #ffffff;
    --ink: #3b3b3b;
    --ink-soft: #555555;
    --brand-green: #6bb57b;
    --brand-orange: #e8711f;
    --stamp-blue: #6f8fcf;
  }
  * { margin: 0; padding: 0; box-sizing: border-box; }
  html, body {
    width: 1200px; height: 898px; overflow: hidden;
    background: var(--backdrop);
    font-family: "Lato", Arial, sans-serif;
    color: var(--ink);
  }
  .letterhead {
    position: absolute; left: 300px; top: 25px;
    width: 600px; height: 848px;
    background: var(--paper);
    box-shadow: 0 8px 24px rgba(90, 70, 40, 0.18);
    overflow: hidden;
  }
  .contact-list {
    position: absolute; right: 44px; top: 46px;
    list-style: none; font-size: 9px; line-height: 15px; color: var(--ink);
  }
  .contact-list li { display: flex; align-items: center; gap: 5px; }
  .contact-list svg { width: 9px; height: 9px; fill: none; stroke: var(--brand-orange); stroke-width: 1.4; }
  .brand {
    position: absolute; left: 46px; top: 112px;
    display: flex; align-items: center; gap: 8px;
  }
  .brand-dot { width: 14px; height: 14px; border-radius: 50%; background: var(--brand-green); }
  .brand-name { font-size: 20px; font-weight: 700; color: var(--ink); line-height: 1.1; }
  .letter-body {
    position: absolute; left: 100px; top: 300px; width: 420px;
    font-size: 10.5px; line-height: 16px; color: var(--ink-soft);
  }
  .letter-body p { margin-bottom: 14px; }
  .letter-body p:last-child { margin-bottom: 0; }
  .sign-off {
    position: absolute; left: 400px; top: 600px; width: 120px;
    font-size: 9.5px; color: var(--ink-soft); text-align: right;
  }
  .signature-area {
    position: absolute; left: 380px; top: 618px; width: 140px; height: 64px;
  }
  .notary-stamp {
    position: absolute; left: 0; top: 2px; width: 58px; height: 58px;
    border: 2px solid var(--stamp-blue); border-radius: 50%; opacity: 0.75;
  }
  .signature-mark {
    position: absolute; left: 68px; top: 16px; width: 72px; height: 24px;
    background: linear-gradient(90deg, rgba(40,40,40,0.15), rgba(40,40,40,0.35));
    border-radius: 10px;
  }
  .footer-band { position: absolute; left: 0; bottom: 0; width: 600px; height: 120px; }
  .footer-address {
    position: absolute; left: 24px; bottom: 9px;
    font-size: 17px; color: #ffffff; letter-spacing: 0.2px;
  }
</style>
</head>
<body>
  <main class="letterhead">
    <ul class="contact-list">
      <li><svg viewBox="0 0 10 10"><path d="M2 1 L4 3 L3 4 Q4.5 6 6 7 L7 6 L9 8 L8 9 Q4 9 1 5 Q1 2 2 1Z"/></svg>555-013-8274</li>
      <li><svg viewBox="0 0 10 10"><rect x="1" y="2" width="8" height="6"/><path d="M1 2 L5 5.5 L9 2"/></svg>office@ferncoveadvice.example</li>
      <li><svg viewBox="0 0 10 10"><circle cx="5" cy="5" r="4"/><path d="M1 5 H9 M5 1 Q2.5 5 5 9 M5 1 Q7.5 5 5 9"/></svg>www.ferncoveadvice.example</li>
    </ul>

    <div class="brand">
      <span class="brand-dot"></span>
      <span class="brand-name">Fern Cove Law Group</span>
    </div>

    <section class="letter-body">
      <p>Lorem ipsum dolor sit amet, consectetur adipiscing elit. Donec orci purus, luctus vitae dignissim eu, iaculis sed purus. Vivamus faucibus, ipsum nec aliquet viverra, leo mauris condimentum ligula, sit amet sagittis enim ligula quis arcu. Nam egestas tortor id nisi porttitor mattis. In tortor ante, ultricies in suscipit a, tempus non massa. Vivamus et auctor mi. Fusce vel massa nulla. Phasellus nec eros mauris, et scelerisque orci.</p>
      <p>Donec malesuada orci vitae nulla accumsan porta a id massa. Quisque accumsan iaculis magna sit amet fringilla. Maecenas consequat, magna eget tincidunt semper, odio nibh rutrum mi, id feugiat ante nisi eu risus. Vestibulum nunc orci, rhoncus a placerat in, ultricies in mi. Cras mattis varius eros, vel fringilla nisi suscipit eget. Quisque scelerisque sagittis nulla at porttitor.</p>
      <p>Sed id augue vitae urna euismod commodo aliquet a quam. Pellentesque arcu velit, cursus et malesuada ut, consequat et diam. Nullam erat sem, rhoncus id ullamcorper vitae, rhoncus et arcu. In ultricies ultricies nulla, ut rutrum nisi iaculis at. Donec eu magna a metus ornare faucibus. Fusce aliquet faucibus ultricies. Morbi semper, est id tincidunt gravida, sem arcu adipiscing lacus, ac bibendum nulla leo eu purus. Quisque nec diam sed risus consectetur accumsan quis quis nibh. Vestibulum id purus lorem.</p>
    </section>

    <div class="sign-off">Sincerely,</div>
    <div class="signature-area">
      <div class="notary-stamp" role="img" aria-label="Notary seal"></div>
      <div class="signature-mark" role="img" aria-label="Handwritten signature"></div>
    </div>

    <svg class="footer-band" viewBox="0 0 600 120" preserveAspectRatio="none">
      <path d="M0 80 C200 80 340 72 440 46 C500 30 550 24 600 22 V28 C550 30 500 36 445 52 C340 80 200 86 0 86Z" fill="var(--brand-green)"/>
      <path d="M0 120 V86 C200 86 340 78 445 52 L470 46 C458 70 452 100 454 120Z" fill="var(--brand-orange)"/>
    </svg>
    <div class="footer-address">Harbor Lane 42, 10115 Millbrook</div>
  </main>
</body>
</html>
```